The Grand Journeys of Tilda Barkaroo and Mabel Moo!

Have you ever wondered how a rescue puppy feels before and after being adopted?
Coming November 2015

The Grand Journeys of Tilda Barkaroo and Mabel Moo, Tilda gets her family

www.tildabarkaroo-example.com sign up to receive updates, special offers and enter contests!

Target Market(s)

children age 4-8, parents of children this age group 30-65

Industry/Entity Type

Publishing Company

Colors
33a6d7
6c459b
a64599

Requirements
Must have
• room for postage, a whimsical feel

```html
<!DOCTYPE html>
<html lang="en">
<head>
<meta charset="utf-8">
<title>The Grand Journeys of Tilda Barkaroo and Mabel Moo! – Postcard</title>
<link href="https://fonts.googleapis.com/css2?family=Oswald:wght@500;700&family=Open+Sans:wght@400;600;700&display=swap" rel="stylesheet">
<style>
  :root {
    --blue: #33a6d7;
    --purple: #6c459b;
    --magenta: #a64599;
    --deep: #4a2a78;
    --ink: #3d3d4a;
    --page: #ececef;
    --card: #ffffff;
    --stamp: #d9d9de;
    --mist: #dfe9f3;
  }
  * { box-sizing: border-box; margin: 0; padding: 0; }
  html, body { width: 900px; height: 1200px; overflow: hidden; }
  body { background: var(--page); font-family: "Open Sans", sans-serif; color: var(--ink); position: relative; }

  .card { position: absolute; left: 60px; width: 780px; height: 520px; background: var(--card); overflow: hidden; box-shadow: 0 2px 10px rgba(0,0,0,.12); }
  .card-front { top: 60px; }
  .card-back { top: 620px; }
  .card svg.shapes { position: absolute; inset: 0; }

  /* Front */
  .title { position: absolute; left: 40px; top: 34px; font-family: "Oswald", sans-serif; font-weight: 700; text-transform: uppercase; line-height: 1.02; }
  .title .line-main { display: block; font-size: 50px; color: var(--purple); letter-spacing: .5px; }
  .title .line-names { display: block; font-size: 31px; color: var(--magenta); }
  .title .line-and { display: block; font-size: 38px; color: var(--deep); }

  .hero-art { position: absolute; left: 70px; top: 195px; width: 250px; height: 240px; border-radius: 40% 45% 20% 30%; background: radial-gradient(circle at 45% 40%, #c9a6e0, #8d62bd 55%, rgba(255,255,255,0) 72%); }

  .story { position: absolute; left: 470px; top: 205px; width: 280px; color: #fff; }
  .story h2 { font-family: "Oswald", sans-serif; font-weight: 700; font-size: 28px; letter-spacing: .5px; margin-bottom: 6px; }
  .story p { font-size: 11.4px; line-height: 1.42; }

  .site-front { position: absolute; right: 30px; bottom: 26px; font-family: "Open Sans", sans-serif; font-weight: 700; font-size: 19px; color: var(--purple); }

  /* Back */
  .flora-art { position: absolute; left: 0; top: 0; width: 400px; height: 235px; background: linear-gradient(135deg, #1f5f9e, var(--blue) 45%, #8fd0ea 75%, #ffffff); }
  .stamp-box { position: absolute; right: 28px; top: 24px; width: 84px; height: 96px; background: var(--stamp); }
  .butterfly-art { position: absolute; left: 330px; top: 135px; width: 110px; height: 110px; border-radius: 50%; border: 4px solid var(--purple); background: radial-gradient(circle, #f0c64a, #c0772a 55%, #3a2a1a); }

  .resources { position: absolute; left: 32px; top: 268px; width: 340px; }
  .resources h3 { font-family: "Oswald", sans-serif; font-weight: 700; font-size: 20px; color: var(--ink); text-transform: uppercase; margin-bottom: 10px; }
  .resource-cols { display: grid; grid-template-columns: 1fr 1fr; column-gap: 26px; }
  .resource { margin-bottom: 10px; }
  .resource h4 { font-size: 10px; font-weight: 700; color: var(--magenta); text-transform: uppercase; line-height: 1.25; margin-bottom: 3px; }
  .resource li { list-style: none; font-size: 10px; line-height: 1.4; color: var(--ink); }

  .back-band { position: absolute; left: 0; bottom: 0; width: 100%; height: 46px; background: linear-gradient(90deg, var(--deep), var(--purple) 60%, var(--magenta)); }
  .site-back { position: absolute; left: 32px; bottom: 13px; font-weight: 700; font-size: 17px; color: #fff; }
</style>
</head>
<body>

<section class="card card-front" aria-label="Postcard front">
  <svg class="shapes" width="780" height="520" viewBox="0 0 780 520" aria-hidden="true">
    <defs>
      <linearGradient id="panelGrad" x1="0" y1="0" x2="1" y2="1">
        <stop offset="0" stop-color="#a64599"/>
        <stop offset=".5" stop-color="#6c459b"/>
        <stop offset="1" stop-color="#4a2a78"/>
      </linearGradient>
      <linearGradient id="mistGrad" x1="0" y1="0" x2="1" y2="0">
        <stop offset="0" stop-color="#ffffff"/>
        <stop offset=".5" stop-color="#dfe9f3"/>
        <stop offset="1" stop-color="#b9d7ee"/>
      </linearGradient>
    </defs>
    <path class="story-panel" d="M780 150 C 640 150, 470 160, 430 200 C 400 240, 420 380, 430 430 L 780 430 Z" fill="url(#panelGrad)"/>
    <path class="story-edge" d="M780 140 C 640 140, 460 150, 420 195" fill="none" stroke="#33a6d7" stroke-width="5"/>
    <path class="footer-mist" d="M0 470 C 200 430, 480 420, 780 400 L 780 520 L 0 520 Z" fill="url(#mistGrad)"/>
  </svg>

  <h1 class="title">
    <span class="line-main">The Grand Journeys</span>
    <span class="line-names">of Tilda Barkaroo</span>
    <span class="line-and">and Mabel Moo</span>
  </h1>

  <div class="hero-art" role="img" aria-label="Illustration of a girl in a purple dress dancing beside a black and white puppy"></div>

  <div class="story">
    <h2>OUR STORY</h2>
    <p>Introducing The Grand Journeys of Tilda Barkaroo and Mabel Moo! The author behind the new children's book series is the talented Marla Quenby Hart. The illustrator that has brought Marla's vision to life is the inspiring Petra L. Vance. Brookfield Press is pleased to provide publishing and editorial consulting. Today marks the launch of the gorgeous website to accompany the series. Please take a look and let us know what you think.</p>
  </div>

  <p class="site-front">www.tildabarkaroo-example.com</p>
</section>

<section class="card card-back" aria-label="Postcard back">
  <div class="flora-art" role="img" aria-label="Whimsical blue floral illustration with a small girl figure"></div>

  <svg class="shapes" width="780" height="520" viewBox="0 0 780 520" aria-hidden="true">
    <defs>
      <linearGradient id="waveGrad" x1="0" y1="0" x2="1" y2="0">
        <stop offset="0" stop-color="#6c459b"/>
        <stop offset="1" stop-color="#a64599"/>
      </linearGradient>
    </defs>
    <path class="wave" d="M0 240 C 160 260, 300 240, 400 200 C 480 170, 560 190, 620 175 L 620 188 C 560 205, 480 190, 400 220 C 300 258, 150 280, 0 258 Z" fill="url(#waveGrad)"/>
    <path class="wave-line" d="M0 266 C 160 290, 300 270, 400 232 C 480 204, 560 216, 620 200" fill="none" stroke="#33a6d7" stroke-width="3"/>
  </svg>

  <div class="butterfly-art" role="img" aria-label="Photo of a golden butterfly in a round frame"></div>
  <div class="stamp-box" aria-label="Postage stamp area"></div>

  <div class="resources">
    <h3>Intersting Resources</h3>
    <div class="resource-cols">
      <div>
        <div class="resource">
          <h4>All About Adopting a Dog</h4>
          <ul><li>Rescue Paws Network</li><li>Second Chance Shelters</li><li>Happy Tails Finder</li><li>Adopt-a-Friend.org</li></ul>
        </div>
        <div class="resource">
          <h4>Shopping for Your Pet</h4>
          <ul><li>Biscuit &amp; Bow</li></ul>
        </div>
      </div>
      <div>
        <div class="resource">
          <h4>How to Find Children's Book Favorites</h4>
          <ul><li>A Bright Reader</li><li>Story Nook Kids</li></ul>
        </div>
        <div class="resource">
          <h4>Everything You Need to Know About Your Furry Best Friend</h4>
          <ul><li>Tails and Tales</li></ul>
        </div>
      </div>
    </div>
  </div>

  <div class="back-band"></div>
  <p class="site-back">www.tildabarkaroo-example.com</p>
</section>

</body>
</html>
```